Pitch Deck and business cards for Virtual Reality Startup

We need a redesign of our pitch deck to be funky, creative and interactive with animated graphics inline with our product (VR training)
Note: the design does not have to be orange that's just a template of the information we're sending you so we would like to see other colours also.

Target Market(s)

Investors

Industry/Entity Type

Media

Contact Information for Business Card

logo, Name, title, address, telephone, email, website

Font styles to use
Other font styles liked:
• funky but readable

Colors

Designer to choose colors to be used in the design.

Requirements
Must have
• Exciting non traditional design that fits a new, innovative, exciting and interactive technology
Nice to have
• .
Should not have
• traditional look and feel.

```html
<!DOCTYPE html>
<html lang="en">
<head>
<meta charset="utf-8">
<title>Team – What makes us unique?</title>
<link rel="stylesheet" href="https://fonts.googleapis.com/css2?family=Montserrat:wght@300;400;800&family=Raleway:wght@400;500&display=swap">
<style>
  :root {
    --blue-base: #0d69b3;
    --blue-deep: #08579c;
    --blue-light: #1683cc;
    --hex-frame: #0a4d92;
    --hex-frame-dark: #073f7c;
    --white: #ffffff;
    --ink: #1a1a1a;
    --photo-light: #eef1f4;
    --photo-mid: #c9b7a6;
  }
  * { box-sizing: border-box; margin: 0; padding: 0; }
  html, body { width: 1200px; height: 728px; overflow: hidden; background: #dcdcdc; }

  .slide {
    position: relative;
    width: 1200px;
    height: 728px;
    overflow: hidden;
    background:
      radial-gradient(ellipse at 55% 40%, var(--blue-light) 0%, rgba(22,131,204,0) 60%),
      linear-gradient(180deg, var(--blue-base) 0%, var(--blue-deep) 100%);
    font-family: "Raleway", sans-serif;
    color: var(--white);
  }

  .slide-title {
    position: absolute;
    left: 66px;
    top: 354px;
    transform: translate(-50%, -50%) rotate(-90deg);
    white-space: nowrap;
    font-family: "Montserrat", sans-serif;
    font-size: 54px;
    line-height: 1;
    letter-spacing: -0.5px;
  }
  .slide-title strong { font-weight: 800; }
  .slide-title span { font-weight: 300; }

  .member {
    position: absolute;
    width: 260px;
    margin-left: -130px;
    text-align: center;
  }
  .member-frame {
    position: relative;
    width: 260px;
    height: 250px;
  }
  .member-frame svg {
    position: absolute;
    left: 0; top: 0;
  }
  .member-photo {
    position: absolute;
    left: 37px;
    top: 18px;
    width: 186px;
    height: 214px;
    clip-path: polygon(50% 0, 100% 25%, 100% 75%, 50% 100%, 0 75%, 0 25%);
    background: linear-gradient(180deg, var(--photo-light) 0%, var(--photo-light) 35%, var(--photo-mid) 100%);
  }
  .member-name {
    font-family: "Montserrat", sans-serif;
    font-weight: 800;
    font-size: 17px;
    letter-spacing: 0.1px;
    text-transform: uppercase;
    white-space: nowrap;
  }
  .member-role {
    font-size: 15.5px;
    font-weight: 500;
    line-height: 21px;
    margin-top: 4px;
  }

  .corner-bar {
    position: absolute;
    left: 0; bottom: 0;
    width: 124px; height: 18px;
    background: var(--white);
  }
  .page-number {
    position: absolute;
    right: 0; bottom: 0;
    width: 51px; height: 38px;
    background: var(--white);
    color: var(--ink);
    font-family: "Montserrat", sans-serif;
    font-size: 14px;
    display: flex; align-items: center; justify-content: center;
  }
</style>
</head>
<body>
<main class="slide">
  <h1 class="slide-title"><strong>What makes</strong> <span>us unique?</span></h1>

  <svg width="0" height="0" style="position:absolute">
    <defs>
      <g id="hex-backdrop">
        <polygon points="130,2 240,60 240,190 130,248 20,190 20,60" fill="var(--hex-frame)"/>
        <polygon points="70,20 130,2 190,20 245,120 190,230 130,248 70,230 15,120" fill="var(--hex-frame-dark)" opacity="0.55"/>
      </g>
    </defs>
  </svg>

  <article class="member" style="left:337px; top:34px;">
    <div class="member-frame">
      <svg width="260" height="250" aria-hidden="true"><use href="#hex-backdrop"/></svg>
      <div class="member-photo" role="img" aria-label="Portrait photo of Marco Hale"></div>
    </div>
    <h2 class="member-name">Marco Hale</h2>
    <p class="member-role">Co Founder and CEO</p>
  </article>

  <article class="member" style="left:641px; top:34px;">
    <div class="member-frame">
      <svg width="260" height="250" aria-hidden="true"><use href="#hex-backdrop"/></svg>
      <div class="member-photo" role="img" aria-label="Portrait photo of Dr Lena Marquez"></div>
    </div>
    <h2 class="member-name">Dr Lena Marquez</h2>
    <p class="member-role">Learning and Development<br>Strategist</p>
  </article>

  <article class="member" style="left:957px; top:34px;">
    <div class="member-frame">
      <svg width="260" height="250" aria-hidden="true"><use href="#hex-backdrop"/></svg>
      <div class="member-photo" role="img" aria-label="Portrait photo of Rosa Tanaki"></div>
    </div>
    <h2 class="member-name">Rosa Tanaki</h2>
    <p class="member-role">Co Founder, Education and<br>Content Director</p>
  </article>

  <article class="member" style="left:337px; top:388px;">
    <div class="member-frame">
      <svg width="260" height="250" aria-hidden="true"><use href="#hex-backdrop"/></svg>
      <div class="member-photo" role="img" aria-label="Portrait photo of Luca Ferrante"></div>
    </div>
    <h2 class="member-name">Luca Ferrante</h2>
    <p class="member-role">360 Film and Post-Production<br>Expert</p>
  </article>

  <article class="member" style="left:641px; top:388px;">
    <div class="member-frame">
      <svg width="260" height="250" aria-hidden="true"><use href="#hex-backdrop"/></svg>
      <div class="member-photo" role="img" aria-label="Portrait photo of Sofia Varela"></div>
    </div>
    <h2 class="member-name">Sofia Varela</h2>
    <p class="member-role">Learnng Designeri</p>
  </article>

  <article class="member" style="left:957px; top:388px;">
    <div class="member-frame">
      <svg width="260" height="250" aria-hidden="true"><use href="#hex-backdrop"/></svg>
      <div class="member-photo" role="img" aria-label="Portrait photo of Kenji Morita"></div>
    </div>
    <h2 class="member-name">Kenji Morita</h2>
    <p class="member-role">Programmer and Game<br>Developer</p>
  </article>

  <div class="corner-bar"></div>
  <div class="page-number">4</div>
</main>
</body>
</html>
```